electrical contracting buisness letter box drop flyer

designed for letter box drop, must look professional.
make use of provided web site/ business card and logo templates for colour schemes.

Target Market(s)

commercial and residential clients for maintenance and comnstruction electrical works

Industry/Entity Type

Electrical

Requirements
Must have
• air conditioning supply and installation pricing list
• test tag pricing
• electrical testing and safety certificate brief
• website and contact details
• make use of the website colour scheme
• A5 single sided format
• State 24-7 call outs
• Pensioner discount of 15% on labour

```html
<!DOCTYPE html>
<html lang="en">
<head>
<meta charset="utf-8">
<title>Brayden Electrical – Letterbox Flyer</title>
<link href="https://fonts.googleapis.com/css2?family=Open+Sans:wght@400;600;700;800&display=swap" rel="stylesheet">
<style>
:root{
  --red:#e42129;
  --navy:#23336b;
  --grey-band:#e6e7e9;
  --text:#3a3a3a;
  --muted:#6b6b6b;
  --white:#ffffff;
}
*{box-sizing:border-box;margin:0;padding:0}
html,body{width:943px;height:1200px;overflow:hidden;background:#f2f2f2}
body{font-family:"Open Sans",Arial,sans-serif;color:var(--text)}
.flyer{position:relative;width:943px;height:1200px;background:var(--white);overflow:hidden}
.hero{position:absolute;left:0;top:0;width:943px;height:386px;
  background:linear-gradient(120deg,#8a6e5d 0%,#c9b9a6 30%,#9aa3a8 55%,#5e6d62 80%,#3f4a44 100%)}
.logo-panel{position:absolute;left:0;top:0}
.brand{position:absolute;left:42px;top:38px;display:flex;align-items:center;gap:12px}
.brand-dot{width:30px;height:30px;border-radius:50%;background:var(--red)}
.brand-name{font-weight:800;color:var(--navy);font-size:30px;line-height:1.05;letter-spacing:1px}
.brand-lic{position:absolute;left:84px;top:112px;font-size:12px;font-weight:700;color:var(--navy);letter-spacing:2px}
.features{position:absolute;left:0;top:386px;width:943px;height:160px;background:var(--grey-band);display:flex;justify-content:space-around;padding:0 18px;z-index:1}
.banner{position:absolute;left:0;top:310px;z-index:2}
.banner-text{position:absolute;left:32px;top:317px;color:var(--white);font-weight:700;font-size:23px;line-height:30px;letter-spacing:.3px;z-index:3}
.banner-icon{position:absolute;left:698px;top:318px;z-index:3}
.feature{width:170px;text-align:center;padding-top:24px}
.feature svg{display:block;margin:0 auto 8px}
.feature p{font-size:11.5px;line-height:16px;color:#444}
.section{position:absolute}
.section h2{color:var(--red);font-size:17px;font-weight:700;padding-bottom:4px;border-bottom:2px solid var(--navy);margin-bottom:18px}
.section p{font-size:11.5px;line-height:15.5px;margin-bottom:11px;text-align:justify}
.section ul{list-style:none}
.section li{position:relative;padding-left:20px;font-size:11.5px;line-height:15.5px;margin-bottom:10px;text-align:justify}
.section li::before{content:"";position:absolute;left:0;top:3px;width:8px;height:8px;border:1.5px solid var(--navy);border-radius:50%}
.small{font-size:8.5px !important;line-height:10px !important}
.price-title{font-size:11.5px;margin:14px 0 10px}
.price-row{display:flex;font-size:11.5px;line-height:15.5px}
.price-row .dots{flex:1;border-bottom:1px dotted #777;margin:0 2px 4px}
.price-row b{width:38px;text-align:right}
.product{position:absolute}
.fineprint{position:absolute;left:488px;top:1083px;width:420px;font-size:7.5px;line-height:8.5px;font-weight:700;color:#222}
.footer-navy{position:absolute;left:0;top:1136px;width:943px;height:64px;background:var(--navy)}
.footer-red{position:absolute;left:0;top:1118px}
.phone{position:absolute;left:106px;top:1128px;color:var(--white);font-weight:700;font-size:31px;letter-spacing:2px}
.phone-icon{position:absolute;left:32px;top:1131px}
.web{position:absolute;right:36px;top:1153px;color:var(--white);font-weight:700;font-size:22px;letter-spacing:2.5px}
</style>
</head>
<body>
<div class="flyer">
  <div class="hero" role="img" aria-label="Photo of an electrician testing a switchboard with a multimeter"></div>
  <svg class="logo-panel" width="520" height="140" viewBox="0 0 520 140">
    <polygon points="0,0 508,0 380,135 0,135" fill="#ffffff"/>
    <polyline points="508,0 380,135" stroke="#9aa0a6" stroke-width="4" fill="none"/>
  </svg>
  <div class="brand">
    <span class="brand-dot"></span>
    <div class="brand-name">BRAYDEN<br>ELECTRICAL</div>
  </div>
  <div class="brand-lic">— EC 24681 —</div>

  <div class="features">
    <div class="feature">
      <svg width="78" height="78" viewBox="0 0 78 78"><circle cx="39" cy="39" r="35" fill="#fff" stroke="#e42129" stroke-width="3"/><rect x="24" y="26" width="30" height="20" rx="4" fill="#23336b"/><text x="39" y="41" text-anchor="middle" fill="#fff" font-size="11" font-weight="700" font-family="Open Sans">%</text><rect x="35" y="48" width="8" height="12" fill="#9aa0a6"/></svg>
      <p>15% Discount On Labour<br>If You Are A Pensioner</p>
    </div>
    <div class="feature">
      <svg width="78" height="78" viewBox="0 0 78 78"><circle cx="39" cy="39" r="35" fill="#fff" stroke="#23336b" stroke-width="3"/><circle cx="39" cy="39" r="17" fill="none" stroke="#e42129" stroke-width="3"/><text x="39" y="43" text-anchor="middle" fill="#e42129" font-size="10" font-weight="800" font-family="Open Sans">24/7</text></svg>
      <p>24/7<br>Call Outs</p>
    </div>
    <div class="feature">
      <svg width="78" height="78" viewBox="0 0 78 78"><circle cx="39" cy="39" r="35" fill="#fff" stroke="#23336b" stroke-width="3"/><circle cx="39" cy="39" r="16" fill="#e42129"/><polyline points="31,39 37,45 47,33" fill="none" stroke="#fff" stroke-width="3.5"/></svg>
      <p>Quality Guarantee<br>On All Works</p>
    </div>
    <div class="feature">
      <svg width="78" height="78" viewBox="0 0 78 78"><circle cx="39" cy="39" r="35" fill="#fff" stroke="#23336b" stroke-width="3"/><rect x="24" y="28" width="30" height="24" fill="none" stroke="#23336b" stroke-width="2.5"/><circle cx="39" cy="24" r="5" fill="#e42129"/><line x1="29" y1="37" x2="49" y2="37" stroke="#e42129" stroke-width="2.5"/><line x1="29" y1="44" x2="49" y2="44" stroke="#e42129" stroke-width="2.5"/></svg>
      <p>Manufacturer's Warranty<br>On All Products</p>
    </div>
    <div class="feature">
      <svg width="78" height="78" viewBox="0 0 78 78"><circle cx="39" cy="39" r="35" fill="#fff" stroke="#23336b" stroke-width="3"/><path d="M39 58 C30 46 27 40 27 34 a12 12 0 0 1 24 0 c0 6-3 12-12 24z" fill="#e42129"/><circle cx="39" cy="34" r="5" fill="#fff"/></svg>
      <p>Locally Owned And Run<br>Business</p>
    </div>
  </div>

  <svg class="banner" width="830" height="90" viewBox="0 0 830 90">
    <polygon points="0,0 805,0 830,88 790,76 0,76" fill="#e42129"/>
  </svg>
  <div class="banner-text">Call us for all your electrical maintenance and<br>renovation needs, no job too big or small.</div>
  <svg class="banner-icon" width="60" height="60" viewBox="0 0 60 60">
    <circle cx="30" cy="30" r="24" fill="none" stroke="#fff" stroke-width="4" stroke-dasharray="120 30"/>
    <text x="30" y="37" text-anchor="middle" fill="#fff" font-family="Open Sans" font-weight="800" font-size="18">24</text>
  </svg>

  <section class="section" style="left:22px;top:562px;width:352px">
    <h2 style="width:262px">RCD's (safety switches)</h2>
    <p>Avoid the legal and moral ramifications of having a non-compliant property, either to live in or when tenanting or selling.</p>
    <ul>
      <li>Brayden electrical can bring your house up to standard by installing and testing the minimum 2 RCD's required by law.</li>
      <li><b>Already have RCD's fitted?</b> Have Brayden Electrical make sure they are installed/functioning correctly and that all required electrical equiptment is appropriatly protected by the fitted switches.</li>
    </ul>
    <p>Brayden Electrical can supply, fit and test 2 Voltra RCBO's to your switchboard from as little as <b>$248.50</b></p>
  </section>
  <div class="product" style="left:382px;top:592px;width:56px;height:118px;background:linear-gradient(#fafafa,#d9d9d9);border-radius:3px" role="img" aria-label="RCD safety switch product"></div>

  <section class="section" style="left:22px;top:888px;width:352px">
    <h2 style="width:262px">Smoke Alarms</h2>
    <p>Make sure your home or investment is safe, rental ready, and legally compliant by having Brayden Electrical install or inspect and test your current smoke alarms.</p>
    <p>Brayden Electrical can supply, fit and test 2 inter connected voltra photoelectric smoke alarms to your premisis starting at <b>$336</b></p>
  </section>
  <div class="product" style="left:370px;top:880px;width:82px;height:62px;border-radius:50%;background:radial-gradient(#ffffff,#cfcfcf)" role="img" aria-label="Smoke alarm product"></div>

  <section class="section" style="left:488px;top:560px;width:330px">
    <h2 style="width:230px">Air Conditioning</h2>
    <p style="margin-bottom:0">See our following price guide for supply and installation of split system air conditioning to your home or office.</p>
    <p class="small">(supply and fit prices are quoted as back to back installations only additional costs may apply for installations that differ).</p>
    <div class="price-title">SPLIT AIR CONDITIONER SUPPLY AND FIT</div>
    <div class="price-row"><span>Kaizen 1.7/2.0kW</span><span class="dots"></span><b>$1199</b></div>
    <div class="price-row"><span>Kaizen 2.0/2.5kW</span><span class="dots"></span><b>$1299</b></div>
    <div class="price-row"><span>Kaizen 2.5/3.2kW</span><span class="dots"></span><b>$1399</b></div>
    <div class="price-row"><span>Kaizen 3.5/4.0kW</span><span class="dots"></span><b>$1599</b></div>
    <div class="price-row"><span>Kaizen 5.0/5.8kW</span><span class="dots"></span><b>$1899</b></div>
    <div class="price-row"><span>Kaizen 6.3/7.1kW</span><span class="dots"></span><b>$2250</b></div>
    <div class="price-row"><span>Kaizen 8.0/9.0kW</span><span class="dots"></span><b>$2850</b></div>
    <p style="margin-top:14px;text-align:left">From <b>$540*</b>, Brayden Electrical can install a supplied standard single storey back to back split system to most homes.</p>
  </section>
  <div class="product" style="left:752px;top:562px;width:168px;height:44px;background:linear-gradient(#ffffff,#dcdcdc);border:1px solid #ccc;border-radius:4px" role="img" aria-label="Split system air conditioner unit"></div>

  <section class="section" style="left:488px;top:888px;width:330px">
    <h2 style="width:230px">LED Downlights</h2>
    <p style="text-align:left">Want to swap an existing light or fan with a 9W led downlight?, or add additional downlights switched of an existing fitting?</p>
    <p style="text-align:left">Brayden electrical can supply and fit Lumo LED downlights in a like for like, or existing switch situation for <b>$59</b> per light.</p>
    <p style="text-align:left">Swap out those dangerous Halogens for a low heat, high efficiency I.C rated LED downlight today.</p>
  </section>
  <div class="product" style="left:830px;top:876px;width:80px;height:38px;border-radius:50%;background:radial-gradient(#ffffff,#d4d4d4)" role="img" aria-label="LED downlight product"></div>
  <svg class="product" style="left:830px;top:930px" width="96" height="30" viewBox="0 0 96 30">
    <circle cx="14" cy="15" r="13" fill="#3b8bc0"/><circle cx="46" cy="15" r="13" fill="#3c9a4a"/><circle cx="78" cy="15" r="13" fill="#222"/>
  </svg>

  <div class="fineprint">(terms and condition apply on all advertised products and services, contact us for details. Advertised prices are GST inclusive. Advertised pricing of goods and services on this flyer are valid until the 01/02/2018)</div>

  <div class="footer-navy"></div>
  <svg class="footer-red" width="400" height="82" viewBox="0 0 400 82">
    <polygon points="0,0 360,0 398,54 0,54" fill="#e42129"/>
  </svg>
  <svg class="phone-icon" width="44" height="44" viewBox="0 0 60 60">
    <circle cx="30" cy="30" r="24" fill="none" stroke="#fff" stroke-width="4" stroke-dasharray="120 30"/>
    <text x="30" y="37" text-anchor="middle" fill="#fff" font-family="Open Sans" font-weight="800" font-size="18">24</text>
  </svg>
  <div class="phone">0491570156</div>
  <div class="web">www.braydenelectrical.com.au</div>
</div>
</body>
</html>
```